wrap white vandrel tallimax 2020

Want a Wow look that will attract attention Please look our website!

looking for a car wrap on Vandrel 2020 white car company website is www.maplelanternservices.com we take care of seniors in their home. we want a clean eye catching design

Target Market(s)

Seniors and famlies that are looking for help with love ones

Industry/Entity Type

Home Health Care

Font styles to use
Serif
Sans Serif

Requirements
Must have
• out company Name: Maple Lantern Services, phone number 410-555-0186: website maplelanternservices.com , quote : Exemplary In -Home Care!
Nice to have
• nice photo

```html
<!DOCTYPE html>
<html lang="en">
<head>
<meta charset="UTF-8">
<title>Maple Lantern Services – Vehicle Wrap</title>
<link href="https://fonts.googleapis.com/css2?family=Playfair+Display:wght@400;500&family=Oswald:wght@500;600&family=Playball&family=Montserrat:wght@600;700&display=swap" rel="stylesheet">
<style>
  :root {
    --blue: #1f67ad;
    --navy: #0f4479;
    --sky: #29a6e4;
    --white: #ffffff;
    --edge: #cfd7df;
    --page: #ffffff;
  }
  html, body {
    margin: 0;
    padding: 0;
    width: 854px;
    height: 1200px;
    overflow: hidden;
    background: var(--page);
  }
  .wrap-sheet { display: block; width: 854px; height: 1200px; }
  .panel-base { fill: var(--white); stroke: var(--edge); stroke-width: 1.5; }
  .field-blue { fill: var(--blue); }
  .field-white { fill: var(--white); }
  .stripe-sky { fill: none; stroke: var(--sky); stroke-width: 9; stroke-linecap: round; }
  .swoosh-sky { fill: var(--sky); }
  .photo-ring { fill: var(--white); }
  .photo-fill { fill: url(#photoTone); }
  .brand-small { font-family: "Playfair Display", serif; font-size: 27px; fill: var(--white); }
  .brand-large { font-family: "Playfair Display", serif; font-size: 38px; fill: var(--white); }
  .phone { font-family: "Oswald", sans-serif; font-weight: 600; font-size: 30px; fill: var(--sky); }
  .tagline { font-family: "Playball", cursive; font-size: 19px; fill: var(--white); }
  .web { font-family: "Montserrat", sans-serif; font-weight: 700; font-size: 10.5px; letter-spacing: 3px; fill: var(--blue); }
  .rear-window { fill: var(--navy); }
  .rear-band { fill: var(--blue); }
  .rear-band-light { fill: var(--sky); opacity: .75; }
  .pill { fill: var(--white); }
  .pill-text { font-family: "Oswald", sans-serif; font-weight: 500; font-size: 11px; fill: var(--navy); }
  .list-item { font-family: "Oswald", sans-serif; font-weight: 500; font-size: 8.5px; fill: var(--white); letter-spacing: .2px; }
  .list-dot { fill: var(--white); }
  .rear-name { font-family: "Playfair Display", serif; font-size: 19px; fill: var(--sky); }
  .rear-phone { font-family: "Oswald", sans-serif; font-weight: 600; font-size: 27px; fill: var(--navy); }
</style>
</head>
<body>
<svg class="wrap-sheet" viewBox="0 0 854 1200" xmlns="http://www.w3.org/2000/svg">
  <defs>
    <linearGradient id="photoTone" x1="0" y1="0" x2="1" y2="1">
      <stop offset="0" stop-color="#e9e2da"/>
      <stop offset=".55" stop-color="#c9b9ab"/>
      <stop offset="1" stop-color="#2f6aa4"/>
    </linearGradient>
    <clipPath id="sideClip"><rect width="774" height="300" rx="40"/></clipPath>
    <g id="sideArt">
      <rect class="panel-base" width="774" height="300" rx="40"/>
      <g clip-path="url(#sideClip)">
        <path class="field-blue" d="M0,0 H290 C335,0 345,55 372,88 C402,122 450,127 540,129 C630,131 682,140 712,190 L762,300 H0 Z"/>
        <path class="stripe-sky" d="M290,0 C335,0 345,55 372,88 C402,122 450,127 540,129 C630,131 682,140 712,190 L762,300"/>
        <path class="swoosh-sky" d="M120,300 C220,250 330,232 420,258 C500,280 590,276 660,240 C690,226 712,244 722,264 L740,300 Z"/>
        <path class="field-white" d="M0,300 V262 C140,236 270,232 370,262 C450,286 560,286 650,254 C680,244 700,252 708,264 L730,300 Z"/>
      </g>
    </g>
  </defs>

  <!-- Driver side -->
  <g class="side side--left" transform="translate(40,40)">
    <use href="#sideArt"/>
    <circle class="photo-ring" cx="170" cy="112" r="100"/>
    <circle class="photo-fill" cx="170" cy="112" r="91" role="img" aria-label="Photo of a smiling caregiver in blue scrubs with an elderly woman holding a cane"/>
    <text class="brand-small" x="290" y="132">Maple</text>
    <text class="brand-large" x="290" y="172">Lantern</text>
    <text class="brand-small" x="290" y="206">Services</text>
    <text class="phone" x="540" y="182" text-anchor="middle">410-555-0186</text>
    <text class="tagline" x="540" y="214" text-anchor="middle">Exemplary In -Home Care!</text>
    <text class="web" x="250" y="284">MAPLELANTERNSERVICES.COM</text>
  </g>

  <!-- Passenger side -->
  <g class="side side--right" transform="translate(40,450)">
    <use href="#sideArt" transform="translate(774,0) scale(-1,1)"/>
    <circle class="photo-ring" cx="626" cy="112" r="100"/>
    <circle class="photo-fill" cx="626" cy="112" r="91" role="img" aria-label="Photo of a smiling caregiver in blue scrubs with an elderly woman holding a cane"/>
    <text class="brand-small" x="386" y="138">Maple</text>
    <text class="brand-large" x="386" y="178">Lantern</text>
    <text class="brand-small" x="386" y="212">Services</text>
    <text class="phone" x="234" y="182" text-anchor="middle">410-555-0186</text>
    <text class="tagline" x="234" y="214" text-anchor="middle">Exemplary In -Home Care!</text>
    <text class="web" x="300" y="284">MAPLELANTERNSERVICES.COM</text>
  </g>

  <!-- Rear -->
  <g class="rear" transform="translate(257,840)">
    <rect class="panel-base" width="340" height="340" rx="30"/>
    <path class="rear-band" d="M0,30 Q0,0 30,0 H310 Q340,0 340,30 V340 H290 C305,250 300,180 280,120 H60 C40,180 35,250 50,340 H0 Z"/>
    <path class="rear-band-light" d="M60,120 C40,180 35,250 50,340 H68 C55,250 60,180 78,120 Z"/>
    <path class="rear-band-light" d="M280,120 C300,180 305,250 290,340 H272 C285,250 280,180 262,120 Z"/>
    <rect class="rear-window" x="32" y="14" width="276" height="106" rx="14"/>
    <rect class="pill" x="112" y="24" width="116" height="17" rx="8.5"/>
    <text class="pill-text" x="170" y="37" text-anchor="middle">What makes us different</text>
    <g class="feature-list">
      <circle class="list-dot" cx="112" cy="52" r="3"/><text class="list-item" x="119" y="55">Owner - Certification Dementia Trainer</text>
      <circle class="list-dot" cx="112" cy="65" r="3"/><text class="list-item" x="119" y="68">Meaningful &amp; Engaging Activities</text>
      <circle class="list-dot" cx="112" cy="78" r="3"/><text class="list-item" x="119" y="81">Home Solutions When Needed</text>
      <circle class="list-dot" cx="112" cy="91" r="3"/><text class="list-item" x="119" y="94">Extensive Care-Partner Education</text>
      <circle class="list-dot" cx="112" cy="104" r="3"/><text class="list-item" x="119" y="107">Nutrition/Local Chef Inspired Training</text>
    </g>
    <text class="rear-name" x="170" y="258" text-anchor="middle">Maple Lantern Services</text>
    <text class="rear-phone" x="170" y="296" text-anchor="middle">410-555-0186</text>
  </g>
</svg>
</body>
</html>
```